Penny Parcel Ad

I need to create a layout with the information on the PDF, but I want you to re-design it and freshen up the look. I've attached a Word Doc with the size and format requirement for the penny parcel print. The PDF I created in illustrator CS6 also has the proper guides.

Target Market(s)

Storm Damaged Areas

Font styles to use
Serif
Sans Serif

Requirements
Must have
• Fresh, clean design. I prefer upscale look versus modern or techy.

```html
<!DOCTYPE html>
<html lang="en">
<head>
<meta charset="utf-8">
<title>True Peak Roofing – Penny Parcel Ad</title>
<link rel="stylesheet" href="https://fonts.googleapis.com/css2?family=Anton&family=Jost:wght@300;400;500;700&family=Oswald:wght@400&display=swap">
<style>
  :root {
    --orange: #f07c1b;
    --orange-light: #ffa040;
    --orange-deep: #e8640c;
    --brown: #4a3330;
    --brown-deep: #3e1a12;
    --brown-light: #7a2f1c;
    --paper: #fbfaf8;
    --ink: #3b3231;
    --badge-red: #d6242a;
    --art-pink: #f3b3d4;
    --art-tan: #f2d6a6;
  }
  * { margin: 0; padding: 0; box-sizing: border-box; }
  html, body { width: 1200px; height: 835px; overflow: hidden; background: #ffffff; }
  .ad {
    position: relative; width: 1200px; height: 835px;
    background: var(--paper); font-family: "Jost", sans-serif; color: var(--ink);
    overflow: hidden;
  }
  .top-band { position: absolute; left: 0; top: 0; width: 100%; height: 27px; background: var(--brown); }
  .top-band::before {
    content: ""; position: absolute; left: 0; top: 0; width: 385px; height: 27px;
    background: var(--orange); clip-path: polygon(0 0, 100% 0, 96% 100%, 0 100%);
  }
  .bottom-band { position: absolute; left: 0; bottom: 0; width: 100%; height: 12px; background: var(--orange); }

  .brand { position: absolute; left: 37px; top: 62px; display: flex; align-items: center; gap: 16px; }
  .brand-dot { width: 70px; height: 70px; border-radius: 50%; background: var(--brown); }
  .brand-name { font-family: "Anton", sans-serif; font-size: 82px; line-height: 1; color: var(--brown); letter-spacing: -1px; }

  .tagline { position: absolute; left: 604px; top: 42px; }
  .tagline-small { font-weight: 300; font-size: 41px; color: var(--orange); line-height: 1.1; }
  .tagline-big { font-weight: 700; font-size: 49px; color: var(--brown-deep); line-height: 1.05; letter-spacing: 0.5px; }

  .coupons { position: absolute; top: 178px; left: 40px; display: flex; gap: 21px; }
  .coupon {
    position: relative; width: 267px; height: 179px;
    clip-path: polygon(14px 0, calc(100% - 14px) 0, 100% 14px, 100% calc(100% - 14px), calc(100% - 14px) 100%, 14px 100%, 0 calc(100% - 14px), 0 14px);
    display: flex; align-items: center; justify-content: center;
  }
  .coupon--orange { background: radial-gradient(ellipse at center, var(--orange-light) 0%, var(--orange) 55%, var(--orange-deep) 100%); }
  .coupon--brown { background: radial-gradient(ellipse at center, var(--brown-light) 0%, #53190f 60%, var(--brown-deep) 100%); }
  .coupon::before {
    content: ""; position: absolute; inset: 6px; border: 2px dotted rgba(255,255,255,0.55);
  }
  .coupon::after {
    content: ""; position: absolute; inset: 14px; border: 1px dashed rgba(255,255,255,0.7); border-radius: 10px;
  }
  .coupon-label { position: relative; z-index: 1; color: #fff; font-size: 41px; font-weight: 400; }

  .feature { position: absolute; top: 386px; font-size: 17px; line-height: 1.4; }
  .feature-title { color: var(--orange); font-size: 19px; display: flex; align-items: center; gap: 9px; margin-left: -26px; }
  .feature-title svg { flex: none; }
  .feature--insured { left: 63px; }
  .feature--quality { left: 376px; }
  .feature--adjusters { left: 631px; }
  .feature--adjusters .feature-title { text-transform: uppercase; font-size: 18px; }

  .partner { position: absolute; left: 972px; top: 389px; display: flex; align-items: center; gap: 15px; }
  .partner-badge { width: 59px; height: 61px; background: var(--badge-red); }
  .partner-text { font-family: "Oswald", sans-serif; font-size: 29px; line-height: 1.08; color: var(--brown-deep); }

  .reviews-banner {
    position: absolute; left: 0; top: 481px; width: 715px; height: 46px;
    background: var(--brown); border-radius: 0 24px 24px 0; color: #fff;
    font-size: 23px; font-weight: 400; line-height: 46px; padding-left: 38px;
    white-space: nowrap;
    box-shadow: 0 3px 4px rgba(0,0,0,0.25);
  }

  .quote-mark { position: absolute; font-family: "Anton", sans-serif; color: var(--orange); font-size: 40px; line-height: 1; }
  .quote-mark--open { left: 36px; top: 548px; }
  .quote-mark--close { left: 330px; top: 704px; }
  .review { position: absolute; left: 75px; top: 552px; width: 736px; font-size: 16.6px; line-height: 23.5px; text-align: justify; }
  .review-author { position: absolute; left: 75px; top: 720px; color: var(--orange); font-weight: 700; font-size: 18px; }

  .roof-art {
    position: absolute; left: 880px; top: 610px; width: 320px; height: 213px;
    background: linear-gradient(135deg, var(--art-pink) 0%, var(--art-tan) 70%);
  }

  .trust { position: absolute; left: 37px; top: 762px; display: flex; align-items: center; gap: 14px; }
  .trust-badge { width: 138px; height: 55px; background: var(--brown-deep); border-radius: 5px; }
  .trust-grade { width: 33px; height: 33px; border-radius: 50%; background: var(--brown-deep); }

  .quote-online { position: absolute; right: 664px; top: 766px; text-align: right; font-size: 20px; line-height: 25px; }
  .quote-online .url { font-size: 20px; display: flex; align-items: center; gap: 6px; justify-content: flex-end; }
  .quote-online .url em { font-style: normal; color: var(--orange); }
  .divider { position: absolute; left: 554px; top: 742px; width: 1px; height: 79px; background: var(--orange); }

  .call-label { position: absolute; right: 395px; top: 744px; font-size: 29px; }
  .phone { position: absolute; left: 583px; top: 778px; display: flex; align-items: center; gap: 12px; }
  .phone-number { font-family: "Oswald", sans-serif; font-weight: 400; color: var(--orange); font-size: 40px; line-height: 1; letter-spacing: 0.5px; }
</style>
</head>
<body>
<main class="ad">
  <div class="top-band"></div>

  <div class="brand">
    <span class="brand-dot"></span>
    <span class="brand-name">True Peak</span>
  </div>

  <div class="tagline">
    <p class="tagline-small">Locally Owned Company</p>
    <p class="tagline-big">Servicing North Texas</p>
  </div>

  <section class="coupons">
    <div class="coupon coupon--orange"><span class="coupon-label">Coupon #1</span></div>
    <div class="coupon coupon--brown"><span class="coupon-label">Coupon #2</span></div>
    <div class="coupon coupon--orange"><span class="coupon-label">Coupon #3</span></div>
    <div class="coupon coupon--brown"><span class="coupon-label">Coupon #4</span></div>
  </section>

  <div class="feature feature--insured">
    <p class="feature-title"><svg width="17" height="17" viewBox="0 0 17 17"><rect x="1" y="1" width="15" height="15" fill="none" stroke="#3b3231" stroke-width="1.5"/><path d="M4 9l3 3 6-8" fill="none" stroke="#3b3231" stroke-width="2"/></svg>Fully Insured Roofing Crews</p>
    <p>we carry both liability coverage and<br>workers compensation for our crews.</p>
  </div>
  <div class="feature feature--quality">
    <p class="feature-title"><svg width="17" height="17" viewBox="0 0 17 17"><rect x="1" y="1" width="15" height="15" fill="none" stroke="#3b3231" stroke-width="1.5"/><path d="M4 9l3 3 6-8" fill="none" stroke="#3b3231" stroke-width="2"/></svg>Quality, Hand nailed roofs</p>
    <p>Ask about our professional<br>installation process.</p>
  </div>
  <div class="feature feature--adjusters">
    <p class="feature-title"><svg width="17" height="17" viewBox="0 0 17 17"><rect x="1" y="1" width="15" height="15" fill="none" stroke="#3b3231" stroke-width="1.5"/><path d="M4 9l3 3 6-8" fill="none" stroke="#3b3231" stroke-width="2"/></svg>Licensed Texas Property Adjusters</p>
    <p>We have experience adjusting claims &amp;<br>will help you close your claim quickly.</p>
  </div>

  <div class="partner">
    <span class="partner-badge"></span>
    <p class="partner-text">PREFERRED<br>CONTRACTOR</p>
  </div>

  <h2 class="reviews-banner">See What Your Neighbors In North Texas Are Saying About Us</h2>

  <span class="quote-mark quote-mark--open">&ldquo;</span>
  <p class="review">I am a very skeptical person when it comes to general contracting and particularly roofing. True Peak put the roof on my mother-in-laws house after the last bad hail storm we had. Sam was at the work site about 90% of the time making sure he was available to not only the crew, but to my mother-in-law as well. He worked well with insurance adjuster and made sure all the paperwork was in order for the insurance company and the bank. You just don't see service like that often. He went on to do my neighbors house as well. Both jobs were done professionally and looked amazing. As long as True Peak is in business, I will continue to refer and use them.</p>
  <span class="quote-mark quote-mark--close">&rdquo;</span>
  <p class="review-author">-Dana R Decatur, TX</p>

  <div class="roof-art" role="img" aria-label="Illustration of a cartoon roofer hammering shingles on a roof"></div>

  <div class="trust">
    <span class="trust-badge"></span>
    <span class="trust-grade"></span>
  </div>

  <div class="quote-online">
    <p>Get a roof quote online!</p>
    <p class="url"><svg width="13" height="13" viewBox="0 0 13 13"><circle cx="6.5" cy="6.5" r="5.5" fill="none" stroke="#f07c1b" stroke-width="1.5"/><path d="M1 6.5h11M6.5 1c-3 3.5-3 7.5 0 11M6.5 1c3 3.5 3 7.5 0 11" fill="none" stroke="#f07c1b" stroke-width="1"/></svg>www.truepeakrc.com/<em>roofquote</em></p>
  </div>
  <div class="divider"></div>

  <p class="call-label">Call Us:</p>
  <div class="phone">
    <svg width="30" height="30" viewBox="0 0 24 24"><path d="M6.6 10.8a15.1 15.1 0 006.6 6.6l2.2-2.2a1 1 0 011-.25 11.4 11.4 0 003.6.57 1 1 0 011 1V20a1 1 0 01-1 1A17 17 0 013 4a1 1 0 011-1h3.5a1 1 0 011 1c0 1.250.2 2.450.57 3.570a1 1 0 01-.25 1z" fill="#3b3231"/></svg>
    <span class="phone-number">555 014 2870</span>
  </div>

  <div class="bottom-band"></div>
</main>
</body>
</html>
```